BW Business Card

Used Car Sales
We are trying to recreate the image of our license plate on business cards,
it is a red background with a white oval that is open on the ends
I attempted to upload the image but it was a dismal failure when the products arrived
the lettering was too small and the edges were white
I think maybe the red needs some texture in it, still red but something that doesn't look so flat
and maybe a beveled edge around the white (not sure)

Target Market(s)

Adults 25-65 that drive

Industry/Entity Type

Business

Contact Information for Business Card

Darlene Whitcombe, Sales Manager, BRIGHTWAY AUTO MART, INC., 462 Fernhill Road, Cedar Hollow, KY 42718,
931 587-2064 (office), 931 587-6259 (fax) - We Finance everyone with approved credit
BrightwayAutoMart.Com

On Back: Financing Available - We Finance everyone with approved credit
Easy Payments: Monthly, Semi-Monthly or Weekly
Ask about our Layaway plan
Open Mon-Sat
8:30 AM - 5 PM

Requirements
Must have
• We want to match the license plate (minus holes for screws)

```html
<!DOCTYPE html>
<html lang="en">
<head>
<meta charset="utf-8">
<title>BW Business Card</title>
<link rel="stylesheet" href="https://fonts.googleapis.com/css2?family=Source+Sans+3:ital,wght@0,400;0,600;0,700;1,400;1,700&display=swap">
<style>
  :root {
    --backdrop: #2a2a2c;
    --plate-red: #c9444b;
    --plate-red-deep: #bd3a41;
    --oval-white: #ffffff;
    --ink-dark: #3a3a40;
    --ink-red: #c23a41;
    --ink-light: #ffffff;
  }
  * { margin: 0; padding: 0; box-sizing: border-box; }
  html, body {
    width: 1200px; height: 1086px; overflow: hidden;
    background: var(--backdrop);
    font-family: "Source Sans 3", "Myriad Pro", Arial, sans-serif;
  }
  .card {
    position: absolute; width: 730px; overflow: hidden;
    background:
      repeating-linear-gradient(0deg, rgba(255,255,255,0.025) 0 1px, transparent 1px 3px),
      repeating-linear-gradient(90deg, rgba(0,0,0,0.03) 0 1px, transparent 1px 4px),
      linear-gradient(160deg, var(--plate-red), var(--plate-red-deep));
  }
  .card--back { left: 132px; top: 90px; height: 453px; }
  .card--front { left: 380px; top: 555px; height: 425px; }
  .card__oval { position: absolute; inset: 0; width: 100%; height: 100%; }
  .line {
    position: absolute; left: 0; width: 100%; height: 40px;
    line-height: 40px; text-align: center; white-space: nowrap;
  }
  .headline { font-size: 57px; font-weight: 700; color: var(--ink-red); letter-spacing: 1.5px; height: 64px; line-height: 64px; }
  .finance-note { font-size: 22.5px; font-weight: 700; color: var(--ink-dark); }
  .payment-terms { font-size: 31px; font-weight: 700; font-style: italic; color: var(--ink-dark); }
  .layaway { font-size: 33.5px; color: var(--ink-light); }
  .hours { font-size: 22px; color: var(--ink-light); }
  .web { font-size: 21px; color: var(--ink-light); }
  .wordmark { font-size: 60px; font-weight: 700; color: var(--ink-dark); letter-spacing: -1px; height: 80px; line-height: 80px; }
  .person-name { font-size: 30px; font-weight: 700; color: var(--ink-red); }
  .person-title { font-size: 17px; font-style: italic; color: var(--ink-dark); height: 24px; line-height: 24px; }
  .contact { font-size: 25px; color: var(--ink-light); }
  .tagline { font-size: 21.5px; color: var(--ink-light); }
  .icon { display: inline-block; vertical-align: -2px; margin-right: 6px; fill: var(--ink-light); }
  .gap { display: inline-block; width: 28px; }
</style>
</head>
<body>

<section class="card card--back">
  <svg class="card__oval" viewBox="0 0 730 453" preserveAspectRatio="none" aria-hidden="true">
    <ellipse cx="365" cy="198" rx="427" ry="110" fill="var(--oval-white)"/>
  </svg>
  <div class="line headline" style="top:136px">FINANCING AVAILABLE</div>
  <div class="line finance-note" style="top:199px">We Finance everyone with approved credit Easy Payments:</div>
  <div class="line payment-terms" style="top:248px">Monthly, Semi-Monthly or Weekly</div>
  <div class="line layaway" style="top:313px">Ask about our Layaway plan</div>
  <div class="line hours" style="top:350px">Open Mon-Sat 8:30 AM - 5 PM</div>
  <div class="line web" style="top:381px">BrightwayAutoMart.Com</div>
</section>

<section class="card card--front">
  <svg class="card__oval" viewBox="0 0 730 425" preserveAspectRatio="none" aria-hidden="true">
    <ellipse cx="365" cy="171" rx="427" ry="109" fill="var(--oval-white)"/>
  </svg>
  <div class="line wordmark" style="top:110px">BrightwayAutoMart.com</div>
  <div class="line person-name" style="top:216px">Darlene Whitcombe</div>
  <div class="line person-title" style="top:250px">Sales Manager</div>
  <div class="line contact" style="top:285px">
    <svg class="icon" width="22" height="16" viewBox="0 0 22 16" aria-hidden="true"><rect x="0" y="0" width="22" height="16"/><path d="M1 1 L11 9 L21 1" fill="none" stroke="#c9444b" stroke-width="1.6"/></svg>462 Fernhill Road, Cedar Hollow, KY 42718,
  </div>
  <div class="line contact" style="top:318px">
    <svg class="icon" width="22" height="18" viewBox="0 0 22 18" aria-hidden="true"><path d="M1 6 Q11 -2 21 6 L18 8 L15 6 L15 4 L7 4 L7 6 L4 8 Z"/><path d="M5 9 L17 9 L20 17 L2 17 Z"/><circle cx="11" cy="13" r="2.2" fill="#c9444b"/></svg>555 587-2064 (office)<span class="gap"></span><svg class="icon" width="18" height="18" viewBox="0 0 18 18" aria-hidden="true"><rect x="4" y="0" width="10" height="7"/><rect x="0" y="7" width="18" height="11"/><rect x="4" y="11" width="10" height="2" fill="#c9444b"/></svg>555 587-6259 (fax)
  </div>
  <div class="line tagline" style="top:350px">We Finance everyone with approved credit BrightwayAutoMart.Com</div>
</section>

</body>
</html>
```